Design WORDPRESS Website for E Commerce Business

We are needing a WORDPRESS website for an E Commerce Business that is supplying quailty kids / baby products.

Target Market(s)

Female / Working Mums / New Mums

Industry/Entity Type

Business

Number of Pages Required

1 page

Font styles to use
Sans Serif

Colors
33b8a4
f8fcfd
d3a5cc
f7f1f7
cbcbcb
9d9d9d

```html
<!DOCTYPE html>
<html lang="en">
<head>
<meta charset="utf-8">
<title>Otter &amp; Kit — Kids &amp; Baby Store</title>
<link rel="stylesheet" href="https://fonts.googleapis.com/css2?family=Questrial&family=Arimo:wght@400;700&display=swap">
<style>
:root{
  --teal:#3b93ab;
  --teal-light:#5fb3c4;
  --pink:#c7607a;
  --ink:#333333;
  --muted:#8a8a8a;
  --line:#e3e3e3;
  --grey-bg:#ececec;
  --footer:#4a4a4a;
  --footer-line:#5c5c5c;
  --white:#ffffff;
  --orange:#e8561c;
  --frame-a:#a35478;
  --frame-b:#c7607a;
  --frame-c:#d9a046;
}
*{margin:0;padding:0;box-sizing:border-box}
html,body{width:1200px;height:3346px;overflow:hidden;background:var(--white)}
body{font-family:"Questrial",sans-serif;color:var(--ink);position:relative}
.abs{position:absolute}

/* header */
.brand{left:85px;top:18px;display:flex;align-items:center;gap:12px}
.brand-dot{width:64px;height:64px;border-radius:50%;background:#8f9aa0}
.brand-name{font-size:34px;line-height:35px;color:var(--teal-light)}
.top-icons{right:76px;top:20px;display:flex;gap:20px}
.top-icons svg{width:16px;height:16px;fill:var(--teal)}
.search{left:848px;top:55px;width:280px;height:38px;border:1px solid #c9c9c9;border-radius:19px;font-size:12px;color:#999;padding:11px 18px}

.nav{left:0;top:105px;width:1200px;height:54px;background:var(--teal);display:flex;align-items:center;padding-left:104px}
.nav a{color:var(--white);font-size:13px;text-decoration:none;text-transform:uppercase;margin-right:56px}

/* hero */
.hero-main{left:85px;top:159px;width:585px;height:529px;background:linear-gradient(135deg,#f4e6d7,#cfe5ee 55%,#8db5dc)}
.hero-top{left:680px;top:159px;width:457px;height:261px;background:linear-gradient(135deg,#9fd0ea,#e9c9a5 55%,#d7463a)}
.hero-bottom{left:680px;top:428px;width:457px;height:260px;background:linear-gradient(135deg,#eef0f0,#b99870 60%,#3a3a3a)}
.badge{left:86px;top:372px;width:258px;height:258px;border-radius:50%;background:var(--pink);border:5px solid rgba(255,255,255,.55);color:var(--white);text-align:center;padding-top:40px}
.badge .pct{font-family:"Arimo",sans-serif;font-size:50px;font-weight:700;line-height:56px;border-top:2px solid #fff;border-bottom:2px solid #fff;display:inline-block;padding:0 6px}
.badge .off{font-size:14px;writing-mode:vertical-rl;transform:rotate(180deg);display:inline-block;vertical-align:middle;margin-left:4px}
.badge .look{font-family:"Arimo",sans-serif;font-size:40px;font-weight:700;line-height:46px;margin-top:8px}

/* features */
.feature{top:722px;width:236px;height:71px;background:var(--teal);color:var(--white);display:flex;align-items:center;padding-left:12px}
.feature svg{width:44px;height:44px;stroke:#fff;fill:none;stroke-width:2;flex:none}
.feature .txt{flex:1;text-align:center;padding-right:8px}
.feature b{display:block;font-weight:400;font-size:14px;letter-spacing:.5px}
.feature small{font-size:10px}

/* products */
.section-title{left:0;width:1200px;text-align:center;font-size:36px;top:875px;letter-spacing:1px;font-weight:400}
.tab{top:965px;height:56px;width:136px;font-size:16px;display:flex;align-items:center;justify-content:center;letter-spacing:1px}
.tab.active{background:var(--pink);color:var(--white)}
.tab.outline{border:2px solid var(--pink);color:var(--ink)}
.card{width:237px;height:384px;border:1px solid var(--line);background:var(--white)}
.card .tag{position:absolute;right:10px;top:8px;background:var(--teal);color:#fff;font-size:10px;padding:3px 12px}
.card .photo{position:absolute;left:48px;top:40px;width:140px;height:150px;border-radius:10px}
.card .name{position:absolute;left:0;top:225px;width:100%;text-align:center;font-size:19px}
.card .meta{position:absolute;left:14px;right:14px;top:278px;display:flex;justify-content:space-between;font-size:13px;color:#555;padding-top:0}
.card .meta s{color:#555}
.card .stars{color:var(--teal);letter-spacing:2px;font-size:13px}
.card .stars i{color:#aaa;font-style:normal}
.card .cart{position:absolute;left:56px;top:322px;width:125px;height:30px;border:1px solid var(--teal);border-radius:15px;font-size:10px;letter-spacing:.5px;display:flex;align-items:center;justify-content:center}

/* partners */
.partners{left:0;top:1957px;width:1200px;height:146px;background:var(--teal)}
.partner{top:38px;width:166px;height:62px;background:var(--white);border:2px solid #dcdcdc}

/* lists */
.lists{left:0;top:2113px;width:1200px;height:474px;background:var(--grey-bg)}
.list{top:75px;width:300px}
.list h3{font-weight:400;font-size:26px;letter-spacing:.5px}
.list hr{width:68px;border:0;border-top:2px solid #b5b5b5;margin:14px 0 30px}
.item{display:flex;gap:24px;margin-bottom:18px;height:62px}
.item .thumb{width:106px;height:62px;background:var(--white);display:flex;align-items:center;justify-content:center;flex:none}
.item .thumb span{width:40px;height:50px;border-radius:6px;display:block}
.item p{font-size:12px;line-height:20px;color:#444}
.item p em{font-style:normal;color:var(--muted);display:block;margin-top:4px}

/* sale */
.sale{left:87px;top:2657px;width:1028px;height:241px;background:linear-gradient(120deg,var(--frame-a),var(--frame-b) 45%,var(--frame-c))}
.sale-inner{left:23px;top:18px;width:982px;height:204px;background:var(--white);text-align:center;padding-top:42px}
.sale-inner h2{font-family:"Arimo",sans-serif;font-weight:700;font-size:44px;color:var(--teal);letter-spacing:1px}
.sale-inner p{font-family:"Arimo",sans-serif;font-weight:700;font-size:35px;color:#555;margin-top:16px;letter-spacing:.5px}
.sale-inner p span{color:var(--pink)}

/* footer */
.footer{left:0;top:2970px;width:1200px;height:376px;background:var(--footer);color:#ddd}
.footer h4{font-weight:400;font-size:13px;letter-spacing:.5px;color:#eee}
.footer .rule{width:34px;border:0;border-top:2px solid var(--orange);margin:8px 0 18px}
.contact-row{display:flex;align-items:center;gap:18px;font-size:12px;line-height:17px;margin-bottom:24px}
.contact-row .ico{width:26px;height:26px;border-radius:50%;background:#3a3a3a;display:flex;align-items:center;justify-content:center;flex:none}
.contact-row svg{width:12px;height:12px;fill:#fff}
.socials{display:flex;gap:10px}
.socials span{width:20px;height:20px;border-radius:50%;background:#fff;display:block}
.footer .blurb{font-size:12px;line-height:22px}
.links{display:grid;grid-template-columns:112px 120px;row-gap:8px;font-size:12px}
.email{width:148px;height:36px;border:1px solid #777;font-size:11px;color:#999;padding:11px 12px}
.go{width:50px;height:36px;background:var(--orange);color:#fff;font-size:14px;display:flex;align-items:center;justify-content:center}
.cards{display:flex;gap:6px}
.cards span{width:52px;height:32px;background:#fff;border-radius:3px;display:block}
.copyright{left:0;top:315px;width:1200px;border-top:1px solid var(--footer-line);padding-top:18px;text-align:center;font-size:12px;color:#bbb}
</style>
</head>
<body>

<header>
  <div class="abs brand">
    <span class="brand-dot"></span>
    <span class="brand-name">Otter<br>&amp; Kit</span>
  </div>
  <div class="abs top-icons">
    <svg viewBox="0 0 16 16"><circle cx="8" cy="5" r="4"/><path d="M1 16c0-4 3-6 7-6s7 2 7 6z"/></svg>
    <svg viewBox="0 0 16 16"><path d="M8 15 1.5 8.5A4 4 0 0 1 8 3a4 4 0 0 1 6.5 5.5z"/></svg>
    <svg viewBox="0 0 16 16"><path d="M0 1h3l2 9h9l2-7H4"/><circle cx="6" cy="14" r="1.5"/><circle cx="13" cy="14" r="1.5"/></svg>
    <svg viewBox="0 0 16 16"><rect x="1" y="1" width="14" height="14"/></svg>
  </div>
  <div class="abs search">Search...</div>
  <nav class="abs nav">
    <a>Home</a><a>Kids clothes</a><a>Footware</a><a>Toy and books</a><a>Moms and maternity</a><a>Shop</a><a>Blog</a><a>Contact us</a>
  </nav>
</header>

<section class="hero">
  <div class="abs hero-main" role="img" aria-label="Photo of two young girls in summer rompers and sun hats"></div>
  <div class="abs hero-top" role="img" aria-label="Photo of a laughing child in a red hood and yellow jacket"></div>
  <div class="abs hero-bottom" role="img" aria-label="Photo of a child in sunglasses and a quilted vest"></div>
  <div class="abs badge">
    <span class="pct">20%</span><span class="off">OFF</span>
    <div class="look">Shop by<br>Look</div>
  </div>
</section>

<section class="features">
  <div class="abs feature" style="left:87px"><svg viewBox="0 0 44 44"><path d="M4 14h22v16H4zM26 20h8l6 6v4H26z"/><circle cx="12" cy="32" r="3"/><circle cx="33" cy="32" r="3"/></svg><div class="txt"><b>FREE SHIPPING</b><small>for all orders over $99</small></div></div>
  <div class="abs feature" style="left:351px"><svg viewBox="0 0 44 44"><path d="M8 38V14h12v24M20 38V6h16v32M4 38h36"/></svg><div class="txt"><b>OFFICIAL STOCKIST</b><small>of more than 100 brands</small></div></div>
  <div class="abs feature" style="left:615px"><svg viewBox="0 0 44 44"><path d="M6 22 22 6h16v16L22 38z"/><circle cx="31" cy="13" r="2"/></svg><div class="txt"><b>2 FREE SAMPLES</b><small>on all orders over $99</small></div></div>
  <div class="abs feature" style="left:878px"><svg viewBox="0 0 44 44"><path d="M12 32a8 8 0 0 1 0-16 11 11 0 0 1 21 3 7 7 0 0 1-1 13z"/><path d="M16 24h12"/></svg><div class="txt"><b>SHOPPER STORE</b><small>rating of 4.9/5</small></div></div>
</section>

<section class="products">
  <h2 class="abs section-title">LATEST PRODUCTS</h2>
  <div class="abs tab active" style="left:377px">ALL</div>
  <div class="abs tab outline" style="left:536px">GIRLS</div>
  <div class="abs tab active" style="left:694px">BOYS</div>

  <article class="abs card" style="left:83px;top:1080px"><span class="tag">New</span><div class="photo" role="img" aria-label="Tiered turquoise and pink girls dress" style="background:linear-gradient(#3fc0c8 60%,#c2409a)"></div><div class="name">LOREM IPSUM</div><div class="meta"><span><s>$10.99</s> / $12.99</span><span class="stars">★★★★<i>☆</i></span></div><div class="cart">ADD TO CART</div></article>
  <article class="abs card" style="left:347px;top:1080px"><span class="tag">New</span><div class="photo" role="img" aria-label="Red glitter girls shoes" style="background:linear-gradient(#fff 35%,#b8141e)"></div><div class="name">LOREM IPSUM</div><div class="meta"><span><s>$10.99</s> / $12.99</span><span class="stars">★★★★<i>☆</i></span></div><div class="cart">ADD TO CART</div></article>
  <article class="abs card" style="left:611px;top:1080px"><span class="tag">New</span><div class="photo" role="img" aria-label="Pink plush character backpack" style="background:linear-gradient(#f4a6c4,#e76a9a)"></div><div class="name">LOREM IPSUM</div><div class="meta"><span><s>$10.99</s> / $12.99</span><span class="stars">★★★★<i>☆</i></span></div><div class="cart">ADD TO CART</div></article>
  <article class="abs card" style="left:875px;top:1080px"><span class="tag">New</span><div class="photo" role="img" aria-label="Red long-sleeve baby romper" style="background:linear-gradient(#e52a2a,#c41616)"></div><div class="name">LOREM IPSUM</div><div class="meta"><span><s>$10.99</s> / $12.99</span><span class="stars">★★★★<i>☆</i></span></div><div class="cart">ADD TO CART</div></article>

  <article class="abs card" style="left:83px;top:1500px"><span class="tag">New</span><div class="photo" role="img" aria-label="Floral print baby headband" style="background:linear-gradient(135deg,#1f3d3a,#e2b46a 50%,#c9454b)"></div><div class="name">LOREM IPSUM</div><div class="meta"><span><s>$10.99</s> / $12.99</span><span class="stars">★★★★<i>☆</i></span></div><div class="cart">ADD TO CART</div></article>
  <article class="abs card" style="left:347px;top:1500px"><span class="tag">New</span><div class="photo" role="img" aria-label="Dark red party dress" style="background:linear-gradient(#7a0d12,#a51c20)"></div><div class="name">LOREM IPSUM</div><div class="meta"><span><s>$10.99</s> / $12.99</span><span class="stars">★★★★<i>☆</i></span></div><div class="cart">ADD TO CART</div></article>
  <article class="abs card" style="left:611px;top:1500px"><span class="tag">New</span><div class="photo" role="img" aria-label="Pink kids cap with animal ears" style="background:linear-gradient(#fff 25%,#e0a39c)"></div><div class="name">LOREM IPSUM</div><div class="meta"><span><s>$10.99</s> / $12.99</span><span class="stars">★★★★<i>☆</i></span></div><div class="cart">ADD TO CART</div></article>
  <article class="abs card" style="left:875px;top:1500px"><span class="tag">New</span><div class="photo" role="img" aria-label="Tiered turquoise and pink girls dress" style="background:linear-gradient(#3fc0c8 60%,#c2409a)"></div><div class="name">LOREM IPSUM</div><div class="meta"><span><s>$10.99</s> / $12.99</span><span class="stars">★★★★<i>☆</i></span></div><div class="cart">ADD TO CART</div></article>
</section>

<section class="abs partners" aria-label="Partner brands">
  <div class="abs partner" style="left:125px"></div>
  <div class="abs partner" style="left:388px"></div>
  <div class="abs partner" style="left:650px"></div>
  <div class="abs partner" style="left:913px"></div>
</section>

<section class="abs lists">
  <div class="abs list" style="left:83px">
    <h3>BEST SELLERS</h3><hr>
    <div class="item"><div class="thumb"><span style="background:#d91f2a"></span></div><p>Lorem Ipsum is simply<br>dummy text of the<em>$10.99 / $12.99</em></p></div>
    <div class="item"><div class="thumb"><span style="background:linear-gradient(#e94a8a 55%,#222)"></span></div><p>Lorem Ipsum is simply<br>dummy text of the<em>$10.99 / $12.99</em></p></div>
    <div class="item"><div class="thumb"><span style="background:#f1a3c0"></span></div><p>Lorem Ipsum is simply<br>dummy text of the<em>$10.99 / $12.99</em></p></div>
  </div>
  <div class="abs list" style="left:463px">
    <h3>POPULAR PRODUCTS</h3><hr>
    <div class="item"><div class="thumb"><span style="background:#d91f2a"></span></div><p>Lorem Ipsum is simply<br>dummy text of the<em>$10.99 / $12.99</em></p></div>
    <div class="item"><div class="thumb"><span style="background:linear-gradient(#e94a8a 55%,#222)"></span></div><p>Lorem Ipsum is simply<br>dummy text of the<em>$10.99 / $12.99</em></p></div>
    <div class="item"><div class="thumb"><span style="background:#f1a3c0"></span></div><p>Lorem Ipsum is simply<br>dummy text of the<em>$10.99 / $12.99</em></p></div>
  </div>
  <div class="abs list" style="left:843px">
    <h3>NEW ARRIVAL</h3><hr>
    <div class="item"><div class="thumb"><span style="background:#d91f2a"></span></div><p>Lorem Ipsum is simply<br>dummy text of the<em>$10.99 / $12.99</em></p></div>
    <div class="item"><div class="thumb"><span style="background:linear-gradient(#e94a8a 55%,#222)"></span></div><p>Lorem Ipsum is simply<br>dummy text of the<em>$10.99 / $12.99</em></p></div>
    <div class="item"><div class="thumb"><span style="background:#f1a3c0"></span></div><p>Lorem Ipsum is simply<br>dummy text of the<em>$10.99 / $12.99</em></p></div>
  </div>
</section>

<section class="abs sale">
  <div class="abs sale-inner">
    <h2>FOR THIS SUMMER</h2>
    <p>SALE UP TO <span>70% OFF</span> GIRLS &amp; BOYS CLOTHINGS</p>
  </div>
</section>

<footer class="abs footer">
  <div class="abs" style="left:110px;top:57px;width:340px">
    <h4>CONTACT INFORMATION</h4><hr class="rule">
    <div class="contact-row"><span class="ico"><svg viewBox="0 0 12 12"><path d="M6 0a4 4 0 0 1 4 4c0 3-4 8-4 8S2 7 2 4a4 4 0 0 1 4-4z"/></svg></span><span>418 Maple Row, Brookfield, IN 46999<br>Hours: 9:00am - 5:00pm CST</span></div>
    <div class="contact-row"><span class="ico"><svg viewBox="0 0 12 12"><path d="M2 0h3l1 3-2 1a7 7 0 0 0 4 4l1-2 3 1v3l-1 2C5 12 0 7 0 1z"/></svg></span><span style="font-weight:700">(555) 014-2290</span></div>
    <div class="contact-row"><span class="ico"><svg viewBox="0 0 12 12"><path d="M0 2h12v8H0zM0 2l6 5 6-5" fill="none" stroke="#fff"/></svg></span><span>hello@otterandkit.com</span></div>
    <div class="socials"><span></span><span></span><span></span><span></span></div>
  </div>
  <div class="abs" style="left:463px;top:57px;width:300px">
    <h4>BE THE FIRST TO KNOW</h4><hr class="rule">
    <p class="blurb">Lorem Ipsum is simply dummy<br>text of the printing and typesetting industry.</p>
    <h4 style="margin-top:30px">MY ACCOUNT</h4><hr class="rule">
    <div class="links"><span>home</span><span>toy and books</span><span>kids clothes</span><span>blog</span><span>footware</span><span>contact us</span></div>
  </div>
  <div class="abs" style="left:856px;top:57px;width:260px">
    <h4>NEWSLETTER</h4><hr class="rule">
    <div style="display:flex;gap:8px"><div class="email">Your Email Id...</div><div class="go">GO</div></div>
    <h4 style="margin-top:26px">PAYMENT OPTIONS</h4><hr class="rule" style="margin-bottom:10px">
    <div class="cards"><span></span><span></span><span></span><span></span></div>
  </div>
  <div class="abs copyright">otterandkit.com 2017. All rights reserved</div>
</footer>

</body>
</html>
```